New business card for Building services company

I own a small 1 person business which primarily works at heights. I gain access to my work areas via ladders and use safety harnesses. I conduct gutter cleaning, roof cleaning with a pressure cleaner(water blaster), ground level pressure cleaning (driveways, footpaths and walls), I also do small handy-man jobs & gardening/ tree trimming.

I have just had a logo designed by Sketch Hive, which I will upload. I'd like to see the themes followed through.
I like the colour of aqua or the colours what is in the logo.

I live in tropical north Queensland in Cairns, Australia. It is where the rain forest meets the Coral Lantern Shoal. On average it is 30+ degrees C.
Updates

Hello all designers. Thankyou for all the submissions so far. The following are my business details which I need on the card-

VERNO Roof, Gutter & Pressure Cleaning Services.
Director -Dale Marwick
Ph 0417385026
Email- roofcleaning@plovernet.example.au
ABN -48 902 317 254

Please include the following services which my business conducts-
*Gutter Cleaning
*Pressure Cleaning- Roof's, Driveways etc
*Minor Roof, Gutter & Building Maintenance
*Garden waste removal & complex cleanups

Public Liability upto $10 Million
Working at Heights Cert.

Quote-                                     Date-

Hi everyone,  could you please ensure you have -"Quote" and "Date" on the card. I'll need space to hand write details on the card for the specific details.        

Requirements
Must have
• The logo attached must be included.
• The rear side of the card is dedicated to job quoted and price of the job.
• *Please include- Quote price, Quote date. etc
• Including the tasks I do at work around the side of the card- Gutter Cleaning; Roof Cleaning, Gutter Maintenance; Gardening; Pressure Cleaning Roof's, Driveways etc.
Nice to have
• The rear side to have a ladder

```html
<!DOCTYPE html>
<html lang="en">
<head>
<meta charset="utf-8">
<title>VERNO – Quote Card, Back</title>
<link rel="stylesheet" href="https://fonts.googleapis.com/css2?family=Cinzel:wght@400;600;700;900&display=swap">
<style>
  :root {
    --page: #ffffff;
    --navy: #283a92;
    --royal: #2b55b8;
    --sky: #1a7ccc;
    --aqua: #00a8a0;
    --teal: #0aa88f;
    --deep-green: #0b7a3f;
    --halo: #f3f0cf;
    --band: rgba(190, 200, 235, 0.45);
    --ink-light: #f4f2e6;
    --ink-dark: #2a3791;
    --ladder-tone: rgba(70, 95, 160, 0.22);
    --black: #0a0a0a;
  }
  * { box-sizing: border-box; margin: 0; padding: 0; }
  html, body { width: 700px; height: 1200px; overflow: hidden; background: var(--page); }
  body { position: relative; font-family: "Cinzel", serif; }

  .card {
    position: absolute; left: 34px; top: 21px; width: 632px; height: 1054px;
    overflow: hidden;
    background:
      radial-gradient(circle at 316px 527px,
        var(--aqua) 0, var(--teal) 180px, var(--sky) 300px, var(--royal) 390px, var(--navy) 500px);
  }

  .brand {
    position: absolute; top: -6px; left: 0; width: 100%;
    text-align: center; font-size: 168px; font-weight: 400;
    letter-spacing: 8px; color: var(--aqua); line-height: 1;
  }
  .tagline {
    position: absolute; top: 162px; width: 100%; text-align: center;
    font-size: 21px; line-height: 26px; color: var(--ink-light); letter-spacing: 0.5px;
  }
  .phone {
    position: absolute; top: 193px; width: 100%; text-align: center;
    font-size: 46px; line-height: 54px; font-weight: 600; color: var(--aqua); letter-spacing: 1px;
  }
  .credentials {
    position: absolute; top: 251px; width: 100%; text-align: center;
    font-size: 24px; line-height: 29px; color: var(--ink-light); letter-spacing: 0.6px;
  }

  .sun {
    position: absolute; left: 227px; top: 438px; width: 178px; height: 178px; border-radius: 50%;
    background: radial-gradient(circle, var(--deep-green) 0, #1f9a57 58%, var(--halo) 72%, rgba(243,240,207,0) 100%);
  }

  .quote-band {
    position: absolute; left: 0; top: 609px; width: 100%; height: 253px;
    background: var(--band);
  }
  .ladder-area {
    position: absolute; left: 180px; top: 609px; width: 286px; height: 253px;
    background: linear-gradient(180deg, rgba(70,95,160,0.08), var(--ladder-tone));
  }

  .field { position: absolute; color: var(--ink-dark); font-size: 40px; line-height: 48px; }
  .field-date { left: 30px; top: 622px; }
  .field-quote { left: 15px; top: 707px; }
  .write-line {
    position: absolute; height: 4px;
    border-bottom: 4px dotted var(--ink-dark);
  }
  .line-1 { left: 196px; top: 655px; width: 386px; }
  .line-2 { left: 196px; top: 740px; width: 386px; }
  .line-3 { left: 210px; top: 787px; width: 388px; }
  .line-4 { left: 210px; top: 835px; width: 388px; }

  .services {
    position: absolute; left: 6px; top: 880px; list-style: none; white-space: nowrap;
    font-size: 23px; line-height: 29px; color: var(--ink-light); letter-spacing: 0.9px;
  }
  .services li::before { content: "* "; }

  .side-label {
    position: absolute; top: 1086px; width: 100%; text-align: center;
    font-size: 96px; font-weight: 700; color: var(--black); line-height: 1;
  }
</style>
</head>
<body>
  <section class="card">
    <div class="brand">VERNO</div>
    <p class="tagline">ROOF, GUTTER &amp; PRESSURE CLEANING SERVECES</p>
    <p class="phone">Call 0417 385 026</p>
    <p class="credentials">Public Liability upto $10 Million<br>Working at Heights Cert.</p>

    <div class="sun"></div>

    <div class="quote-band"></div>
    <div class="ladder-area" role="img" aria-label="Faint ladder rising toward the sun"></div>

    <span class="field field-date">Date&nbsp;&nbsp;&nbsp;:</span>
    <span class="field field-quote">Quote :</span>
    <span class="write-line line-1"></span>
    <span class="write-line line-2"></span>
    <span class="write-line line-3"></span>
    <span class="write-line line-4"></span>

    <ul class="services">
      <li>Gutter Cleaning</li>
      <li>Pressure Cleaning-Roofs,Driveways etc</li>
      <li>Minor Roof,Gutter &amp; Building Maintenance</li>
      <li>Garden waste removal &amp; compled cleanups</li>
    </ul>
  </section>

  <p class="side-label">BACK</p>
</body>
</html>
```